Marrowfield Contracting Business Cards

Front of card:

Full Logo
Name
Address
Office Phone
Cell Phone
Email
Website

Back:
Logo Mark in background
List and markets and services performed

```html
<!DOCTYPE html>
<html lang="en">
<head>
<meta charset="utf-8">
<title>Marrowfield Contracting Business Cards</title>
<link rel="stylesheet" href="https://fonts.googleapis.com/css2?family=Poppins:wght@400;500&family=Orbitron:wght@700&display=swap">
<style>
  :root {
    --bg: #ececec;
    --paper: #fafafa;
    --red: #d51f26;
    --grey: #77777a;
    --ink: #3a3a3c;
    --charcoal: #2b2b2d;
    --charcoal-deep: #222224;
    --ring: #333336;
  }
  * { box-sizing: border-box; margin: 0; padding: 0; }
  html, body { width: 1200px; height: 802px; overflow: hidden; background: var(--bg); }
  .sheet {
    width: 1200px; height: 802px;
    display: flex; align-items: center; justify-content: center; gap: 40px;
  }
  .card {
    position: relative; width: 540px; height: 309px; overflow: hidden;
    box-shadow: 0 6px 18px rgba(0,0,0,.15);
  }

  /* front */
  .card-front { background: var(--paper); border-bottom: 4px solid var(--red); }
  .brand {
    position: absolute; top: 32px; right: 40px;
    display: flex; align-items: center; gap: 12px;
  }
  .brand-dot { width: 46px; height: 46px; border-radius: 50%; background: var(--red); }
  .brand-name {
    font-family: "Orbitron", sans-serif; font-weight: 700; font-size: 17px; line-height: 1.2;
    color: var(--red); letter-spacing: .5px;
  }
  .brand-name small { display: block; font-size: 8px; letter-spacing: 4px; text-align: right; }
  .brand-rule {
    position: absolute; top: 108px; right: 40px; width: 200px; height: 1px; background: var(--grey);
  }
  .person { position: absolute; left: 40px; top: 150px; width: 240px; }
  .person-name {
    font-family: "Orbitron", sans-serif; font-weight: 700; font-size: 15px;
    color: var(--red); letter-spacing: .5px;
  }
  .person-role { font-family: "Poppins", sans-serif; font-size: 12px; color: var(--grey); margin-top: 2px; }
  .person-rule { height: 1px; background: var(--grey); margin: 8px 0 10px; width: 200px; }
  .contact { list-style: none; font-family: "Poppins", sans-serif; font-size: 12px; color: var(--ink); }
  .contact li { display: flex; align-items: center; gap: 8px; line-height: 20px; }
  .contact svg { width: 11px; height: 11px; fill: none; stroke: var(--red); stroke-width: 1.6; }
  .address {
    position: absolute; right: 40px; top: 176px; text-align: right;
    font-family: "Poppins", sans-serif; font-size: 12px; color: var(--grey); line-height: 1.5;
  }
  .footer-band { position: absolute; left: 0; bottom: 0; width: 100%; height: 40px; }
  .website {
    position: absolute; right: 40px; bottom: 8px;
    font-family: "Poppins", sans-serif; font-size: 12px; color: #fff; letter-spacing: .3px;
  }

  /* back */
  .card-back {
    background: linear-gradient(135deg, var(--charcoal) 0%, var(--charcoal-deep) 100%);
    border-bottom: 4px solid var(--red);
  }
  .mark-circle {
    position: absolute; right: -24px; top: -12px; width: 290px; height: 290px; border-radius: 50%;
    background: var(--ring); box-shadow: inset 0 2px 6px rgba(255,255,255,.06), 0 2px 8px rgba(0,0,0,.35);
  }
  .back-name {
    position: absolute; left: 34px; bottom: 50px;
    font-family: "Orbitron", sans-serif; font-weight: 700; font-size: 22px; line-height: 1.15;
    color: var(--red); letter-spacing: .5px;
  }
  .back-name small { display: block; font-size: 9px; letter-spacing: 5px; text-align: right; margin-top: 2px; }
  .back-rule { position: absolute; left: 34px; bottom: 36px; width: 220px; height: 1px; background: #bdbdbd; }
</style>
</head>
<body>
<main class="sheet">
  <section class="card card-front" aria-label="Card front">
    <div class="brand">
      <span class="brand-dot"></span>
      <div class="brand-name">MARROWFIELD<br>CONTRACTING<small>LLC</small></div>
    </div>
    <div class="brand-rule"></div>

    <div class="person">
      <div class="person-name">DANIEL HARLOW</div>
      <div class="person-role">Manager</div>
      <div class="person-rule"></div>
      <ul class="contact">
        <li><svg viewBox="0 0 12 12"><path d="M2 1.5h2.5l1 2.5-1.5 1a6 6 0 0 0 3 3l1-1.5 2.5 1v2.5A9 9 0 0 1 2 1.5z"/></svg>123-456-2100</li>
        <li><svg viewBox="0 0 12 12"><rect x="3" y="1" width="6" height="10" rx="1"/><path d="M5.5 9h1"/></svg>123-456-2100</li>
        <li><svg viewBox="0 0 12 12"><rect x="1" y="2.5" width="10" height="7"/><path d="M1 2.5l5 4 5-4"/></svg>youremail@marrowfield.com</li>
      </ul>
    </div>

    <div class="address">Your Address, City<br>State, Zip 0000</div>

    <svg class="footer-band" viewBox="0 0 540 40" preserveAspectRatio="none" aria-hidden="true">
      <polygon points="0,34 250,34 264,20 540,20 540,24 266,24 252,38 0,38" fill="#8a8a8d"/>
      <polygon points="262,40 278,6 540,6 540,40" fill="#d51f26"/>
    </svg>
    <div class="website">www.yourwebsite.com</div>
  </section>

  <section class="card card-back" aria-label="Card back">
    <div class="mark-circle"></div>
    <div class="back-name">MARROWFIELD<br>CONTRACTING<small>LLC</small></div>
    <div class="back-rule"></div>
  </section>
</main>
</body>
</html>
```